KRV Holdfast Manufacturer New Web Design

We need a new theme designed for metal fastener manufacturing company, KRV Holdfast Group, a $60M division of Benmore Forge Holdings, Inc. We manufacture screw, pins and washers to industrial customers (non-Automotive) such as Tallow Appliance, Marcus Fenwold, BRU, Veltrin, etc. Our current website is www.holdfastparts.example. We would like to stick with the same logo/color scheme, however, I'm aiming to modernize the website's look and feel.

Here are some of our competitor's websites:
- https://www.torvanix.example/
- http://quellbrook.example/
- http://www.morrowbuiltcouplingworks.example/
- http://pegsandoddments.example/
- http://www.dunmerebolting.example/

Target Market(s)

We primarily want to target engineers working in the following markets:
- Appliance (Tallow Appliance, Kelvanor)
- Ag (Fenwold, BRU)
- Recreational Vehicle (Veltrin, Briar Fox)
- Outdoor Power (Oldmeadow, Vexa)

We secondarily want to target buyers working at the above markets as well as buyers at Fastener distributors such as Boltrin, Provision Dynamics, Hollis Parfet.

Industry/Entity Type

Metal Forging

Number of Pages Required

1 page

Requirements
Must have
• For products: "Threaded" product as the primary focus. "Pins" product is the secondary focus, followed by all others.
• Please use same logo and color scheme as I do not plan to change.
Nice to have
• Highlight our featured proprietary products (pamphlets attached). KRV Holdfast's KIN-V, LumDrive, Holdfast Spiral, Pelmont.

```html
<!DOCTYPE html>
<html lang="en">
<head>
<meta charset="utf-8">
<title>KRV Holdfast – Products</title>
<link href="https://fonts.googleapis.com/css2?family=Open+Sans:wght@400;600;700&display=swap" rel="stylesheet">
<style>
  :root {
    --brand-blue: #0288d1;
    --accent-green: #17a58b;
    --text-grey: #555b61;
    --tint: #f3f4f5;
    --white: #ffffff;
  }
  * { margin: 0; padding: 0; box-sizing: border-box; }
  html, body { width: 1200px; height: 1200px; overflow: hidden; background: var(--white); }
  body { position: relative; font-family: "Open Sans", Arial, sans-serif; }

  .tint-block { position: absolute; background: var(--tint); }
  .title-band { position: absolute; width: 600px; height: 79px; background: var(--brand-blue); color: var(--white); }
  .title-band h2 { position: absolute; top: 10px; font-size: 24px; font-weight: 700; letter-spacing: 3.5px; }
  .title-band p { position: absolute; top: 47px; font-size: 16px; font-weight: 400; letter-spacing: 1.3px; }
  .product-photo { position: absolute; width: 600px; }

  .copy { position: absolute; width: 400px; }
  .copy h3 { color: var(--accent-green); font-size: 16px; font-weight: 400; line-height: 19.2px; letter-spacing: 0.6px; margin-bottom: 4px; white-space: nowrap; }
  .copy p { color: var(--text-grey); font-size: 11.4px; line-height: 14.3px; letter-spacing: 0.3px; white-space: nowrap; }
  .explore-btn { position: absolute; width: 119px; height: 40px; background: var(--brand-blue); color: var(--white); font-size: 12px; letter-spacing: 0.5px; display: flex; align-items: center; justify-content: center; text-decoration: none; }
</style>
</head>
<body>

<!-- Pins -->
<section class="product product-pins">
  <div class="tint-block" style="left:468px; top:30px; width:620px; height:144px;"></div>
  <div class="title-band" style="left:0; top:78px;">
    <h2 style="left:122px;">PINS</h2>
    <p style="left:206px;">Secure, Removable Solution</p>
  </div>
  <div class="product-photo" role="img" aria-label="Photo of threaded pins with black square heads" style="left:0; top:157px; height:238px; background:linear-gradient(180deg,#e4e5ea,#d3d4d9);"></div>
  <div class="copy" style="left:720px; top:141px;">
    <h3>Our Pin business is the traditional<br>Marlowe Pinworks product line.</h3>
    <p>Since 1929, KRV Marlowe Pinworks has been leading the industry in<br>a variety of manufacturing processes performed in-house at<br>significant cost savings to the customers. Our expertise<br>covers: Cold heading, cross-hole drilling, grooving/shaving,<br>CNC operations, roll forming, broaching, grinding, and<br>lanyard production. These capabilities, along with our<br>engineering staff, have allowed us to focus on working with<br>customers to solve all of their fastener problems.</p>
  </div>
  <a class="explore-btn" href="#" style="left:720px; top:324px;">Explore</a>
</section>

<!-- Stampings -->
<section class="product product-stampings">
  <div class="tint-block" style="left:114px; top:474px; width:619px; height:144px;"></div>
  <div class="title-band" style="left:600px; top:514px;">
    <h2 style="left:150px;">STAMPNIGS</h2>
    <p style="left:318px;">Diverse and Unique</p>
  </div>
  <div class="product-photo" role="img" aria-label="Photo of polished chrome lobed stamped washers" style="left:600px; top:594px; height:238px; background:linear-gradient(160deg,#8a8d92 0%,#3b3d41 45%,#121314 100%);"></div>
  <div class="copy" style="left:125px; top:561px;">
    <h3>KRV Holdfast Group is the largest,<br>most diverse and uniquely tooled<br>producer of stampings products in the world.</h3>
    <p>Since its 1923 invention of the Twisted Tooth Lock Washer,<br>Holdfast has continued to invent products that<br>revolutionized the stampings industry. Such product<br>inventions as the Square Cones, Spring Washers,<br>Internal/External Lock Washers and Shaft Retainers are the<br>finest anti-vibration, anti-loosening, mechanical fastening<br>devices available today.</p>
  </div>
  <a class="explore-btn" href="#" style="left:125px; top:753px;">Explore</a>
</section>

<!-- Threaded -->
<section class="product product-threaded">
  <div class="tint-block" style="left:468px; top:913px; width:620px; height:143px;"></div>
  <div class="title-band" style="left:0; top:960px;">
    <h2 style="left:101px;">THREADED</h2>
    <p style="left:226px;">Revolutionizing the industry</p>
  </div>
  <div class="product-photo" role="img" aria-label="Photo of steel bolts, screws and washers on a wooden surface" style="left:0; top:1039px; height:161px; background:linear-gradient(180deg,#a8a8a6,#6b6b6a);"></div>
  <div class="copy" style="left:720px; top:961px;">
    <h3>KRV Holdfast Group has developed<br>multiple innovative screw designs such<br>products as KIN-V, QZ Self Extruding, Gripwind<br>&nbsp;and the Mistral, that have gone on to become<br>industry standards.</h3>
    <p>Our new VANTA Technology is again, revolutionizing the<br>industry, in the design and manufacturing of threaded<br>solutions. The VANTA Technology allows our engineers to<br>develop superior thread geometries to tackle your most<br>demanding applications. The industry's most innovative<br>platform of threaded products—the LumDrive, the<br>Holdfast Spiral, and the Holdfast Spiral, are ready<br>to conquer your most difficult design challenges.</p>
  </div>
</section>

</body>
</html>
```